Website for Healthy Energy Bars

I need the layout for a website that will allow customers to purchase three different energy bars. It should have a slide show of pictures on the front page and the following tabs: About, Nutrition Info, FAQ

The website colors should not conflict with the colors of the company logo. Other than that I am open to design ideas and concepts.

Target Market(s)

Health-Conscious Eaters

Industry/Entity Type

Purchase

Number of Pages Required

3 page

Requirements
Must have
• Logo and pictures of the product
Should not have
• Colors that conflict with the logo colors

```html
<!DOCTYPE html>
<html lang="en">
<head>
<meta charset="utf-8">
<title>Verdabar – Healthy Energy Bars</title>
<link href="https://fonts.googleapis.com/css2?family=Roboto+Condensed:wght@300;400;700&family=Open+Sans:wght@400;600&display=swap" rel="stylesheet">
<style>
:root{
  --maroon:#5a1a1f;
  --maroon-dark:#461317;
  --maroon-deep:#36100f;
  --green:#4f9a1f;
  --green-light:#6fb52e;
  --hero-bg:#e8e8e8;
  --beige:#f2ece3;
  --text:#555;
  --muted:#8a8a8a;
  --white:#fff;
}
*{margin:0;padding:0;box-sizing:border-box}
html,body{width:791px;height:1200px;overflow:hidden}
body{font-family:"Open Sans",sans-serif;color:var(--text);background:var(--white);position:relative}
.heading{font-family:"Roboto Condensed",sans-serif}

/* header */
.site-header{height:80px;position:relative;background:var(--white)}
.brand{position:absolute;left:28px;top:20px;display:flex;align-items:center;gap:8px}
.brand-dot{width:26px;height:26px;border-radius:50%;background:var(--green)}
.brand-name{font-family:"Roboto Condensed",sans-serif;font-weight:700;font-size:30px;color:var(--green)}
.account-links{position:absolute;right:30px;top:8px;display:flex;gap:20px;font-size:10px;color:var(--muted)}
.account-links span::before{content:"";display:inline-block;width:7px;height:7px;background:#bbb;border-radius:2px;margin-right:4px}
.cart-button{position:absolute;right:30px;top:40px;background:var(--green);color:var(--white);font-size:10px;padding:5px 14px;border-radius:3px}

/* nav */
.main-nav{height:32px;background:var(--maroon);display:flex;align-items:stretch;padding-left:40px;position:relative}
.main-nav a{font-family:"Roboto Condensed",sans-serif;color:var(--white);font-size:12px;text-decoration:none;padding:0 16px;display:flex;align-items:center}
.main-nav a.active{background:var(--green)}
.search-button{position:absolute;right:30px;top:4px;width:24px;height:24px;background:var(--maroon-dark);display:flex;align-items:center;justify-content:center}

/* hero */
.hero{height:340px;background:var(--hero-bg);position:relative}
.hero-visual{position:absolute;left:40px;top:24px;width:300px;height:270px;border-radius:8px;background:linear-gradient(135deg,#f4efe2 0%,#e9d86a 45%,#8cbf3f 100%)}
.hero-copy{position:absolute;left:370px;top:48px}
.hero-kicker{font-size:25px;font-weight:300;color:#555;letter-spacing:1px}
.hero-title{font-size:37px;font-weight:700;color:var(--maroon);line-height:1.05;margin-top:4px}
.hero-tagline{font-size:24px;font-weight:400;color:var(--green);line-height:1.1;margin-top:6px}
.btn{display:inline-block;background:var(--green);color:var(--white);font-family:"Roboto Condensed",sans-serif;font-weight:700;text-decoration:none;border-radius:3px}
.hero-copy .btn{font-size:15px;padding:10px 22px;margin-top:18px}
.slide-dots{position:absolute;left:50%;bottom:22px;transform:translateX(-50%);display:flex;gap:8px}
.slide-dots i{width:10px;height:10px;border-radius:50%;background:#c8c8c8}
.slide-dots i.on{background:#888}

/* products */
.products{position:relative;height:290px}
.product-card{position:absolute;top:18px;width:205px;height:255px;text-align:center}
.product-card:nth-child(1){left:52px}
.product-card:nth-child(2){left:292px}
.product-card:nth-child(3){left:532px}
.product-visual{height:95px;border-radius:4px;background:linear-gradient(180deg,#f6f1e2,#d9c27a)}
.product-card:nth-child(2) .product-visual{background:linear-gradient(180deg,#f5ece6,#b9414a)}
.product-card:nth-child(3) .product-visual{background:linear-gradient(180deg,#f1e8de,#6b3b22)}
.product-body{background:var(--white);box-shadow:0 2px 6px rgba(0,0,0,.15);padding:12px 14px 14px;height:160px}
.product-name{font-size:16px;font-weight:700;color:var(--maroon);line-height:1.1}
.product-text{font-size:9.5px;line-height:1.45;color:var(--muted);margin-top:8px}
.product-body .btn{font-size:10px;padding:6px 14px;margin-top:10px}

/* welcome */
.welcome{position:absolute;left:0;top:742px;width:791px;height:170px;background:var(--beige)}
.welcome-title{position:absolute;left:40px;top:22px;font-size:34px;font-weight:400;color:#555}
.welcome-title b{color:var(--green);font-weight:700}
.welcome-text{position:absolute;left:40px;top:72px;width:480px;font-size:10px;line-height:1.55;color:var(--muted)}
.read-more{position:absolute;left:40px;top:140px;font-size:10px;font-weight:600;color:var(--maroon)}
.welcome-visual{position:absolute;right:50px;top:8px;width:170px;height:155px;border-radius:50%;background:radial-gradient(circle at 40% 40%,#c9463e,#6a9e2c 60%,#4b7a22)}

/* footer */
.site-footer{position:absolute;left:0;top:912px;width:791px;height:264px;background:var(--maroon-dark);color:#d8c4c4}
.footer-col{position:absolute;top:30px}
.footer-col h3{font-family:"Roboto Condensed",sans-serif;font-size:17px;font-weight:400;color:var(--white);line-height:1.1;margin-bottom:12px;letter-spacing:.5px}
.footer-col ul{list-style:none;font-size:10px;line-height:1.75}
.col-links{left:40px}
.col-news{left:185px;width:165px}
.col-tweets{left:395px;width:175px}
.col-contact{left:600px;width:170px}
.news-text{font-size:9.5px;line-height:1.45;margin-bottom:10px}
.field{height:20px;background:var(--maroon-deep);font-size:9.5px;color:#bba;padding:4px 8px;margin-bottom:6px}
.col-news .btn{font-size:9px;padding:4px 10px}
.tweet{font-size:9.5px;line-height:1.45;margin-bottom:10px}
.tweet small{display:block;color:#a98;font-size:8.5px}
.view-all{font-size:9px;color:var(--green-light)}
.contact-row{display:flex;align-items:flex-start;gap:8px;font-size:10px;margin-bottom:10px}
.social{display:flex;gap:8px;margin-top:6px}
.social i{width:18px;height:18px;border-radius:50%;background:var(--maroon-deep)}
.copyright{position:absolute;left:0;top:1176px;width:791px;height:24px;background:var(--maroon-deep);color:#c9b2b2;font-size:9.5px;text-align:center;line-height:24px}
</style>
</head>
<body>

<header class="site-header">
  <div class="brand"><span class="brand-dot"></span><span class="brand-name">Verdabar</span></div>
  <div class="account-links"><span>My Account</span><span>My Wishlist</span><span>Check Out</span><span>Login</span></div>
  <div class="cart-button">Cart $0.00</div>
</header>

<nav class="main-nav">
  <a href="#" class="active">HOME</a>
  <a href="#">ABOUT</a>
  <a href="#">NUTRITION</a>
  <a href="#">INFO</a>
  <a href="#">FAQ</a>
  <a href="#">CONTACT</a>
  <span class="search-button">
    <svg width="13" height="13" viewBox="0 0 13 13"><circle cx="5.5" cy="5.5" r="4" fill="none" stroke="#fff" stroke-width="1.6"/><line x1="8.5" y1="8.5" x2="12" y2="12" stroke="#fff" stroke-width="1.8"/></svg>
  </span>
</nav>

<section class="hero">
  <div class="hero-visual" role="img" aria-label="Golden pecan chew bar box with pecan nuts and fruit"></div>
  <div class="hero-copy heading">
    <div class="hero-kicker">BOOST YOUR ENERGY WITH</div>
    <div class="hero-title">GOLDEN PECAN<br>CHEW BAR</div>
    <div class="hero-tagline">ENERGY BARS<br>WITH HEALTH &amp; TASTE</div>
    <a href="#" class="btn">VIEW DETAILS</a>
  </div>
  <div class="slide-dots"><i class="on"></i><i></i><i></i></div>
</section>

<section class="products">
  <article class="product-card">
    <div class="product-visual" role="img" aria-label="Golden pecan chew bar package"></div>
    <div class="product-body">
      <h2 class="product-name heading">GOLDEN PECAN<br>CHEW BAR</h2>
      <p class="product-text">Chewy plant bar with roasted pecans and golden oats for steady, natural energy all day long.</p>
      <a href="#" class="btn">VIEW DETAILS</a>
    </div>
  </article>
  <article class="product-card">
    <div class="product-visual" role="img" aria-label="Berry walnut chew bar package"></div>
    <div class="product-body">
      <h2 class="product-name heading">BERRY WALNUT<br>CHEW BAR</h2>
      <p class="product-text">Tart berries and crunchy walnuts blended into a bright, fruity bar for an easy lift.</p>
      <a href="#" class="btn">VIEW DETAILS</a>
    </div>
  </article>
  <article class="product-card">
    <div class="product-visual" role="img" aria-label="Cocoa hazel crunch bar package"></div>
    <div class="product-body">
      <h2 class="product-name heading">COCOA HAZEL<br>CRUNCH BAR</h2>
      <p class="product-text">Dark cocoa and toasted hazelnuts with a satisfying crunch to power your afternoon break.</p>
      <a href="#" class="btn">VIEW DETAILS</a>
    </div>
  </article>
</section>

<section class="welcome">
  <h1 class="welcome-title heading">WELCOME TO <b>VERDABAR</b></h1>
  <p class="welcome-text">Verdabar makes honest energy bars from whole plant ingredients. Every bar is packed with nuts, fruit and seeds, free from artificial additives, and made to keep you going through work, training and travel. We believe good food should taste great and fuel a healthy life every single day.</p>
  <a class="read-more">READ MORE</a>
  <div class="welcome-visual" role="img" aria-label="Bowl of fresh fruit with kiwi, berries and green leaves"></div>
</section>

<footer class="site-footer">
  <div class="footer-col col-links">
    <h3>QUICK LINKS</h3>
    <ul><li>HOME</li><li>ABOUT US</li><li>NUTRITION</li><li>INFO</li><li>FAQ</li><li>CONTACT US</li></ul>
  </div>
  <div class="footer-col col-news">
    <h3>NEWSLETTER<br>SIGN UP</h3>
    <p class="news-text">Get news on new flavours and offers.</p>
    <div class="field">Name</div>
    <div class="field">Email Address</div>
    <a class="btn">SUBMIT</a>
  </div>
  <div class="footer-col col-tweets">
    <h3>LATEST TWEETS</h3>
    <p class="tweet">Fresh batch of pecan bars ships this week. Grab yours before they go!<small>2 hours ago</small></p>
    <p class="tweet">Our new cocoa hazel bar is now in stock for all members.<small>5 hours ago</small></p>
    <span class="view-all">view all tweets</span>
  </div>
  <div class="footer-col col-contact">
    <h3>CONTACT US</h3>
    <div class="contact-row">
      <svg width="10" height="13" viewBox="0 0 10 13"><path d="M5 0a4.5 4.5 0 0 0-4.5 4.5C.5 8 5 13 5 13s4.5-5 4.5-8.5A4.5 4.5 0 0 0 5 0z" fill="#6fb52e"/><circle cx="5" cy="4.5" r="1.6" fill="#461317"/></svg>
      <span>Verdabar,<br>Greenway, Street 12</span>
    </div>
    <div class="contact-row">
      <svg width="11" height="11" viewBox="0 0 11 11"><path d="M2 0l2 2.5-1.2 1.5a7 7 0 0 0 4.2 4.2L8.5 7 11 9l-1.5 2C4.5 11 0 6.5 0 1.5z" fill="#6fb52e"/></svg>
      <span>311 555 0142</span>
    </div>
    <div class="contact-row">
      <svg width="12" height="9" viewBox="0 0 12 9"><rect width="12" height="9" fill="#6fb52e"/><path d="M0 0l6 5 6-5" fill="none" stroke="#461317" stroke-width="1"/></svg>
      <span>hello@verdabar.com</span>
    </div>
    <div class="social"><i></i><i></i><i></i></div>
  </div>
</footer>
<div class="copyright">Copyright 2016 VERDABAR | All Rights Reserved</div>

</body>
</html>
```